KO-TRA , Artificial hedge flyer

i need new flyer, in att i'm sending old one but as we produce artificial flowers, trees and most popular is artificial green hedge, and it's used from variety places, from swimming pool, restaurants, bars, private terrace, gardens, to protect from neighbor :-) . from beginning is all our product, it's not imported from other producer. we are doing it by measure what we get from customer ( tailor made ) , we give guaranty 15-20 years on all weather that will not loos color, etc.. you can see some pictures in att on old flyer, and some new pictures of same in space newly added. we'd like more pictures with samples of use, etc.you can see our product on www.ko-tra.hr so you can closely known what we are producing, and what for we need new flyer. we have plenty of new picture that are not on our web, so i can use it for new flyer.

Font styles to use
Sans Serif

Requirements
Must have
• company logo, contact info ( sent in word document in att ), logo of croatian product ( on old flyer in att on front side), stamp Quality since 1950 if you could change year to 1960, last time they made mistake and write 1950 ),
Nice to have
• flyer 3 fold type, or if you think it will look better only double side flyer, depend of design and theme so everyone can understand what is our business

```html
<!DOCTYPE html>
<html lang="hr">
<head>
<meta charset="utf-8">
<title>KO-TRA – letak</title>
<link rel="stylesheet" href="https://fonts.googleapis.com/css2?family=Marcellus&family=Montserrat:wght@500;600;700;800&family=Great+Vibes&display=swap">
<style>
  :root {
    --backdrop: #02291e;
    --leaf-dark: #2f7a22;
    --leaf-mid: #4e9d2f;
    --flat-green: #6ab545;
    --lime: #a9cc3c;
    --white: #ffffff;
    --logo-grey: #7b7f84;
  }
  * { margin: 0; padding: 0; box-sizing: border-box; }
  html, body { width: 1200px; height: 800px; overflow: hidden; background: var(--backdrop); }
  .canvas { position: relative; width: 1200px; height: 800px; background: var(--backdrop); }

  .page { position: absolute; top: 126px; width: 412px; height: 546px; overflow: hidden; }
  .page--front { left: 152px; }
  .page--back { left: 636px; }

  .foliage { position: absolute; inset: 0; }
  .page--front .foliage {
    background:
      radial-gradient(circle at 30% 25%, rgba(255,255,255,.10), transparent 45%),
      linear-gradient(180deg, var(--leaf-mid) 0%, var(--leaf-dark) 35%, var(--leaf-mid) 55%, var(--flat-green) 72%, var(--flat-green) 100%);
  }
  .page--back .foliage {
    background:
      linear-gradient(180deg, var(--flat-green) 0%, var(--flat-green) 28%, rgba(106,181,69,.6) 42%, transparent 60%),
      radial-gradient(circle at 70% 70%, rgba(255,255,255,.08), transparent 50%),
      linear-gradient(180deg, var(--leaf-mid), var(--leaf-dark) 70%, var(--leaf-mid));
  }

  .frame { position: absolute; border: 5px solid var(--white); }
  .page--front .frame { left: 14px; top: 46px; width: 384px; height: 487px; }
  .page--back .frame { left: 16px; top: 14px; width: 384px; height: 520px; }

  .logo-plate {
    position: absolute; left: 94px; top: 27px; width: 184px; height: 48px;
    background: var(--white); display: flex; align-items: center; justify-content: center; gap: 8px;
  }
  .logo-plate .dot { width: 20px; height: 20px; border-radius: 50%; background: var(--logo-grey); }
  .logo-plate .name {
    font-family: "Montserrat", sans-serif; font-weight: 700; font-size: 19px; color: var(--logo-grey); white-space: nowrap;
  }

  .vertical-title { color: var(--white); }
  .vertical-title span {
    position: absolute; display: block; white-space: nowrap;
    transform-origin: 0 0; transform: rotate(-90deg);
    font-family: "Montserrat", sans-serif; line-height: 1;
  }
  .vertical-title .sub { left: 48px; top: 419px; font-weight: 500; font-size: 24px; }
  .vertical-title .main { left: 98px; top: 419px; font-weight: 800; font-size: 52px; letter-spacing: 1px; }

  .stamp { position: absolute; left: 214px; top: 205px; width: 118px; height: 118px; }

  .front-copy {
    position: absolute; left: 22px; top: 452px; width: 356px;
    font-family: "Montserrat", sans-serif; font-weight: 600; font-size: 11.2px; line-height: 1.3; color: var(--white);
  }

  .headline { position: absolute; left: 0; width: 100%; text-align: center; color: var(--white); font-family: "Marcellus", sans-serif; }
  .headline--prema { top: 30px; font-size: 86px; line-height: 1; letter-spacing: 2px; }
  .headline--dims { top: 120px; font-size: 45px; line-height: 1; letter-spacing: 1px; }
  .tagline-script { position: absolute; top: 163px; left: 0; width: 100%; text-align: center; font-family: "Great Vibes", cursive; font-size: 36px; color: var(--white); }
  .services { position: absolute; top: 216px; left: 0; width: 100%; text-align: center; font-family: "Marcellus", sans-serif; font-size: 28px; line-height: 1.4; color: var(--white); letter-spacing: .5px; }

  .contact-bar {
    position: absolute; left: 34px; top: 430px; width: 348px; height: 74px;
    background: var(--lime); color: var(--white); font-style: normal;
    font-family: "Montserrat", sans-serif; font-weight: 700; font-size: 11.5px; line-height: 1.3;
  }
  .contact-item { position: absolute; display: flex; gap: 8px; align-items: flex-start; }
  .contact-item svg { flex: none; width: 13px; height: 13px; margin-top: 1px; }
  .contact-item--address { left: 8px; top: 10px; }
  .contact-item--phone { left: 204px; top: 10px; }
  .contact-item--mail { left: 8px; top: 50px; }
  .contact-item--web { left: 204px; top: 50px; }
</style>
</head>
<body>
<main class="canvas">

  <section class="page page--front">
    <div class="foliage" role="img" aria-label="Fotografija zelene živice od lišća"></div>
    <div class="frame"></div>
    <div class="logo-plate"><span class="dot"></span><span class="name">KO-TRA d.o.o.</span></div>
    <h1 class="vertical-title">
      <span class="sub">UNUTARNJE I VANJSKO</span>
      <span class="main">UREĐENJE</span>
    </h1>
    <svg class="stamp" viewBox="0 0 116 116" role="img" aria-label="Pečat kvalitete">
      <circle cx="58" cy="58" r="54" fill="none" stroke="#ffffff" stroke-width="4"/>
      <circle cx="58" cy="58" r="44" fill="none" stroke="#ffffff" stroke-width="2"/>
    </svg>
    <p class="front-copy">poslovnih, stambenih, sportskih i ostalih objekata umjetnom živicom, dekorativnim zelenilom i cvijećem, drvećem i aranžmanima</p>
  </section>

  <section class="page page--back">
    <div class="foliage" role="img" aria-label="Fotografija zelene živice od lišća"></div>
    <div class="frame"></div>
    <h2 class="headline headline--prema">PREMA</h2>
    <h2 class="headline headline--dims">DIMENZIJAMA</h2>
    <p class="tagline-script">i željama kupaca</p>
    <p class="services">UNUTARNJE<br>I VANJSKO<br>UREĐENJE PROSTORA</p>

    <address class="contact-bar">
      <div class="contact-item contact-item--address">
        <svg viewBox="0 0 14 14"><circle cx="7" cy="7" r="7" fill="#fff"/><path d="M7 3.2a2.4 2.4 0 0 0-2.4 2.4C4.6 7.5 7 10.8 7 10.8s2.4-3.3 2.4-5.2A2.4 2.4 0 0 0 7 3.2z" fill="#a9cc3c"/></svg>
        <span>LIPOVA ULICA 8, BREZJE<br>10430 SAMOBOR</span>
      </div>
      <div class="contact-item contact-item--phone">
        <svg viewBox="0 0 14 14"><circle cx="7" cy="7" r="7" fill="#fff"/><path d="M4.6 3.6l1.3-.2.7 1.8-.9.7a5 5 0 0 0 2.4 2.4l.7-.9 1.8.7-.2 1.3c-3.4.2-6-2.4-5.8-5.8z" fill="#a9cc3c"/></svg>
        <span>+385 91 555 0142<br>+385 95 555 0187</span>
      </div>
      <div class="contact-item contact-item--mail">
        <svg viewBox="0 0 14 14"><circle cx="7" cy="7" r="7" fill="#fff"/><rect x="3.5" y="4.6" width="7" height="4.8" fill="#a9cc3c"/><path d="M3.5 4.6L7 7.4l3.5-2.8" stroke="#fff" stroke-width=".8" fill="none"/></svg>
        <span>info@ko-tra.hr</span>
      </div>
      <div class="contact-item contact-item--web">
        <svg viewBox="0 0 14 14"><circle cx="7" cy="7" r="7" fill="#fff"/><circle cx="7" cy="7" r="3.6" fill="none" stroke="#a9cc3c" stroke-width="1"/><path d="M3.4 7h7.2M7 3.4v7.2" stroke="#a9cc3c" stroke-width=".8"/></svg>
        <span>www.ko-tra.hr</span>
      </div>
    </address>
  </section>

</main>
</body>
</html>
```